Need to design a business card with logo

Hellow
we are a company ,
PT REKA LINTAS MANDIRI
looking for design of name card.
what we do is property development and management.
design preferable professional corporate look and feel.
corporate. color, pantone colour 289
information required is
company name " Reka Lintas Mandiri"
person name eg " Peter Hollis"
person title eg "secret agent"
address: 9 kestrel road , jakarta, indonesia
phone : +6221 5906471
mobile : 0813 294 615
email : peter@hollistran.com
website: www.peterhol.com
if you want to include logo in the design you are welcome and appreciated , or you can simply use the company name as the logo.
thanks
corporate , business person , show events, exhibition events ,etc
Business

```html
<!DOCTYPE html>
<html lang="en">
<head>
<meta charset="utf-8">
<title>Reka Lintas Mandiri – Business Card</title>
<link rel="stylesheet" href="https://fonts.googleapis.com/css2?family=Signika:wght@400;600&display=swap">
<style>
  :root {
    --navy: #10213f;
    --navy-deep: #0d1b35;
    --steel: #5b7f98;
    --steel-light: #7593ab;
    --steel-dark: #456a88;
    --glow: #8d9ab0;
    --paper: #ffffff;
  }
  * { box-sizing: border-box; margin: 0; padding: 0; }
  html, body {
    width: 1200px;
    height: 308px;
    overflow: hidden;
    background: var(--paper);
    font-family: "Signika", sans-serif;
  }
  .canvas { position: relative; width: 1200px; height: 308px; }

  /* Front of card */
  .card-front { position: absolute; left: 0; top: 0; width: 553px; height: 308px; }
  .front-panel {
    position: absolute; left: 0; top: 0; width: 553px; height: 236px;
    background: var(--navy);
    overflow: hidden;
  }
  .front-band {
    position: absolute; left: 0; top: 235px; width: 553px; height: 6px;
    background: var(--steel);
  }
  .tower-illustration {
    position: absolute; left: 150px; top: 0; width: 250px; height: 236px;
    background:
      linear-gradient(180deg, rgba(170,190,210,0.55) 0%, rgba(95,125,155,0.55) 55%, rgba(200,210,225,0.7) 100%) 72px 4px / 108px 232px no-repeat,
      radial-gradient(ellipse 125px 120px at 50% 48%, rgba(141,154,176,0.75) 0%, rgba(60,80,110,0.35) 55%, rgba(16,33,63,0) 100%);
  }
  .holder-name {
    position: absolute; left: 16px; top: 184px;
    font-size: 20px; font-weight: 600; color: var(--steel-light); line-height: 1;
  }
  .holder-title {
    position: absolute; left: 30px; top: 207px;
    font-size: 15px; font-weight: 400; color: var(--steel-light); line-height: 1;
  }
  .front-contact {
    position: absolute; right: 17px; top: 194px;
    text-align: right; font-size: 13px; line-height: 16px; color: var(--steel-light);
  }
  .company-block {
    position: absolute; left: 0; top: 244px; width: 553px; text-align: center;
  }
  .company-name {
    font-size: 22px; font-weight: 600; color: var(--steel-dark); line-height: 26px;
  }
  .company-address {
    font-size: 12px; color: var(--steel-dark); line-height: 16px;
  }
  .sep { display: inline-block; width: 1px; height: 12px; background: var(--steel-dark); margin: 0 2px; vertical-align: -2px; }

  /* Back of card */
  .card-back {
    position: absolute; left: 645px; top: 0; width: 555px; height: 308px;
    background: var(--navy);
    overflow: hidden;
  }
  .wave-pattern {
    position: absolute; left: 0; top: 0; width: 555px; height: 308px;
    background:
      radial-gradient(ellipse 200px 60px at 18% 52%, rgba(91,127,152,0.18) 0%, rgba(16,33,63,0) 100%),
      radial-gradient(ellipse 130px 150px at 72% 45%, rgba(91,127,152,0.2) 0%, rgba(16,33,63,0) 100%);
  }
  .back-name {
    position: absolute; left: 0; top: 132px; width: 555px; text-align: center;
    font-size: 34px; font-weight: 600; color: var(--steel); line-height: 1; letter-spacing: 0.3px;
  }
</style>
</head>
<body>
<main class="canvas">
  <section class="card-front">
    <div class="front-panel">
      <div class="tower-illustration" role="img" aria-label="Glowing illustration of a tall glass tower made of vertical bars"></div>
      <p class="holder-name">Peter Hollis</p>
      <p class="holder-title">secret agent</p>
      <p class="front-contact">peter@hollistran.com<br>www.peterhol.com</p>
    </div>
    <div class="front-band"></div>
    <div class="company-block">
      <p class="company-name">Reka Lintas Mandiri</p>
      <p class="company-address">9 kestrel road<span class="sep"></span>jakarta, indonesia</p>
      <p class="company-address">+6221 5906471<span class="sep"></span>0813 294 615</p>
    </div>
  </section>

  <section class="card-back">
    <div class="wave-pattern" role="img" aria-label="Fine flowing line waves across the card"></div>
    <p class="back-name">Reka Lintas Mandiri</p>
  </section>
</main>
</body>
</html>
```